Brontaro Web Site

Redesigned web site for Brontaro Ltd (www.brontaro-example.co.uk). This is to feature new logo (attached). Brontaro Ltd is a company which specialises in Geographic Information Systems and Geographic data - we call ourselves GIS Data Specialists. We are looking for something which conveys our professionalism and our experience. There will be more pages than on the current Brontaro website. There will be: Home, Data Migration, Data Cleansing & Validation, Data Analysis, Data Maintenance, Data Quality and an About Us page. All these should be accessible from each page on the website.
Updates
I didn't really think to say that the content of the web site is going to change from the current one we have. There will be more pages than on the current one. They will be: Home, Data Migration, Data Cleansing & Validation, Data Analysis, Data Maintenance, Data Quality and an About Us page. All these should be accessible from each page on the website. I didn't really think through the fact that the number of pages / areas to access can influence the layout of the site, sorry.
Target Market(s)
Utility Companies (e.g. telecommunications providers, energy companies), local government.
Industry/Entity Type
It Company
Look and feel

```html
<!DOCTYPE html>
<html lang="en">
<head>
<meta charset="utf-8">
<title>Brontaro – GIS Data Specialists</title>
<link rel="stylesheet" href="https://fonts.googleapis.com/css2?family=Bebas+Neue&family=Open+Sans:wght@400;700&display=swap">
<style>
:root{
  --page-grey:#e6e6e6;
  --top-light:#f4f4f4;
  --nav-top:#8fd0e2;
  --nav-bottom:#4fa9c6;
  --nav-line:#3a8aa6;
  --nav-text:#0d2a36;
  --hero-dark:#03142b;
  --hero-mid:#0a3d78;
  --hero-bright:#1a9ad8;
  --teal-title:#8ed3dc;
  --body-grey:#9a9a9a;
  --strong-grey:#878787;
  --heading-grey:#8a8a8a;
  --footer-top:#86cbe0;
  --footer-bottom:#5bb3cf;
  --white:#ffffff;
}
*{margin:0;padding:0;box-sizing:border-box}
html,body{width:1200px;height:1000px;overflow:hidden}
body{position:relative;background:var(--page-grey);font-family:"Open Sans",sans-serif}
.masthead{position:absolute;left:0;top:0;width:1200px;height:107px;background:linear-gradient(#fbfbfb,#e2e2e2)}
.utility-tab{position:absolute;left:845px;top:0;width:195px;height:32px;background:linear-gradient(#fff,#f0f0f0);border-radius:0 0 18px 18px;box-shadow:0 3px 6px rgba(0,0,0,.08);display:flex;justify-content:center;align-items:center;font-size:14px;color:#8a8a8a}
.utility-tab a{color:inherit;text-decoration:none;padding:0 14px}
.utility-tab a+a{border-left:1px solid #cfcfcf}
.main-nav{position:absolute;left:0;top:76px;width:1200px;height:31px;background:linear-gradient(var(--nav-top),var(--nav-bottom));border-top:1px solid #5aa6c0;border-bottom:1px solid var(--nav-line)}
.main-nav ul{list-style:none;position:absolute;left:385px;top:0;display:flex;height:30px}
.main-nav li{border-left:1px solid var(--nav-line);border-right:1px solid #a6dcea;height:30px;display:flex;align-items:center;padding:0 10px;font-size:13px;color:var(--nav-text);letter-spacing:.2px}
.logo-tab{position:absolute;left:132px;top:0;width:252px;height:107px;background:linear-gradient(#f7f7f7,#ececec);border-radius:0 0 10px 10px;box-shadow:0 1px 3px rgba(0,0,0,.15);display:flex;align-items:center;padding-left:14px;gap:10px}
.logo-dot{width:40px;height:40px;border-radius:50%;background:#7fcfd8}
.logo-name{font-size:30px;font-weight:700;color:#7a7a7a;line-height:1}
.logo-sub{font-size:14px;color:#7a7a7a;margin-top:2px;font-weight:400}
.hero{position:absolute;left:0;top:107px;width:1200px;height:290px;background:radial-gradient(ellipse 70% 90% at 60% 110%,var(--hero-bright),var(--hero-mid) 55%,var(--hero-dark))}
.hero h1{position:absolute;left:122px;top:40px;font-family:"Bebas Neue",sans-serif;font-weight:400;font-size:31px;color:#e6e6e6;letter-spacing:.3px}
.hero p{position:absolute;left:122px;top:92px;width:335px;font-size:15px;line-height:24px;color:var(--white)}
.btn-learn{position:absolute;left:122px;top:227px;width:112px;height:40px;background:linear-gradient(#fff,#d9d9d9);border-radius:3px;font-family:"Bebas Neue",sans-serif;font-size:25px;color:#111;display:flex;align-items:center;justify-content:center}
.world-map{position:absolute;left:500px;top:20px;width:530px;height:205px;background:radial-gradient(ellipse at center,rgba(120,150,200,.35),rgba(80,110,170,.12) 70%,transparent);border-radius:40%}
.hero-contact{position:absolute;left:847px;top:224px;font-size:13px;line-height:18px;color:var(--white)}
.intro-panel{position:absolute;left:100px;top:420px;width:958px;height:366px;background:linear-gradient(#fff 60%,#f0f0f0);border:1px solid #cfcfcf;border-radius:3px}
.intro-panel h2{position:absolute;left:0;top:16px;width:100%;text-align:center;font-family:"Bebas Neue",sans-serif;font-weight:400;font-size:31px;color:var(--heading-grey)}
.intro-panel h2 span{border-bottom:2px solid var(--heading-grey);line-height:28px;display:inline-block}
.pillar{position:absolute;top:64px;width:224px}
.pillar h3{text-align:center;font-size:19px;font-weight:700;color:var(--teal-title);margin-bottom:11px}
.pillar p{font-size:14px;line-height:18px;color:var(--body-grey);letter-spacing:.3px}
.pillar strong{color:var(--strong-grey)}
.pillar-divider{position:absolute;top:72px;width:1px;height:230px;background:linear-gradient(#e4e4e4,transparent)}
.site-footer{position:absolute;left:0;top:803px;width:1200px;height:197px;background:linear-gradient(var(--footer-top),var(--footer-bottom));border-top:1px solid #4c9ebb;color:var(--white);font-size:13px;line-height:18px}
.sitemap{position:absolute;left:186px;top:16px;list-style:none}
.footer-heading{font-weight:700}
.globe{position:absolute;left:513px;top:18px;width:110px;height:110px;border-radius:50%;background:radial-gradient(circle at 40% 35%,#f5f8f8,#9fb2b5 45%,#1e3538)}
.address{position:absolute;left:857px;top:16px;font-style:normal}
.copyright{position:absolute;left:0;top:170px;width:100%;text-align:center}
</style>
</head>
<body>
<header class="masthead">
  <nav class="utility-tab"><a>Home</a><a>Contact</a></nav>
</header>
<nav class="main-nav">
  <ul>
    <li>Data Migration</li>
    <li>Data Cleansing &amp; Validation</li>
    <li>Data Analysis</li>
    <li>Data Maintenance</li>
    <li>Data Quality</li>
  </ul>
</nav>
<div class="logo-tab">
  <div class="logo-dot"></div>
  <div><div class="logo-name">Brontaro</div><div class="logo-sub">GIS Data Specialists</div></div>
</div>

<section class="hero">
  <h1>Welcome to Brontaro</h1>
  <p>Brontaro was founded in 1994 by a group of geospatial software engineers that recognised the significant value that data, and the systems used to store and analyse this data, could bring to business.</p>
  <div class="btn-learn">Learn More</div>
  <div class="world-map" role="img" aria-label="Striped world map graphic"></div>
  <div class="hero-contact">
    Telephone: +44 (0)1632 960 360<br>
    Fax: +44 (0)1632 960 303<br>
    email: contact@brontaro-example.co.uk
  </div>
</section>

<section class="intro-panel">
  <h2><span>What does it take to be a GIS data specialist?</span></h2>
  <div class="pillar" style="left:16px">
    <h3>Experience</h3>
    <p>We have worked with over 200 companies in a myriad of market sectors - from <strong>utilities, local and central government, oil and gas</strong>, to many spheres of the <strong>marine industry</strong>.</p>
  </div>
  <div class="pillar-divider" style="left:238px"></div>
  <div class="pillar" style="left:251px">
    <h3>Knowledge</h3>
    <p>We provide a vast bank of <strong>knowledge and experience</strong> to offer an all <strong>encompassing service</strong>. This ensures that you, as a customer, reap the <strong>maximum benefits</strong> from your data and systems through utilising a combination of our <strong>skilled consultants, analysts and developers</strong> that will work with you and your requirements to <strong>help achieve your business objectives</strong>.</p>
  </div>
  <div class="pillar-divider" style="left:478px"></div>
  <div class="pillar" style="left:489px">
    <h3>Professionalism</h3>
    <p>We have a wide ranging skill set including <strong>PROJEX 2</strong> qualified Project Managers, fully qualified <strong>Software Developers</strong> and <strong>Experienced Data Consultants</strong>.</p>
  </div>
  <div class="pillar-divider" style="left:718px"></div>
  <div class="pillar" style="left:730px">
    <h3>Independence</h3>
    <p>Brontaro are <strong>platform independent</strong> and have established development partnerships with many of the world's leading GIS product vendors such as <strong>Gridline Network Systems, MapVista, Draftwise, Terralis</strong> and <strong>Bramwell</strong>. These partnerships enhance our ability to react to non-standard requests.</p>
  </div>
</section>

<footer class="site-footer">
  <ul class="sitemap">
    <li class="footer-heading">Sitemap</li>
    <li>Home</li>
    <li>About us</li>
    <li>Data Migration</li>
    <li>Data Cleansing &amp; Validation</li>
    <li>Data Analysis</li>
    <li>Data Maintenance</li>
    <li>Data Quality</li>
    <li>Contact Us</li>
  </ul>
  <div class="globe" role="img" aria-label="Glossy globe illustration"></div>
  <address class="address">
    <span class="footer-heading">Brontaro Ltd</span><br>
    Kelmoor Business Centre<br>
    North Quay Road<br>
    Kelmoor<br>
    Northshire<br>
    KM12 4XY<br>
    Scotland, UK
  </address>
  <div class="copyright">© 2010 Brontaro Ltd. Registered in Scotland No. 482917</div>
</footer>
</body>
</html>
```